Business Card Design Project

We are looking to redesign the logo, business card and stationary of one of our group companies - KESTRAL SUPPLY COMPANY LLC.

The company specialises in industrial PVC and CPVC Piping systems. It is situated in the Middle East and the focus is purely in this region.

The logo work is already completed. The file is uploaded for the reference.

We are looking for a clean minimalistic design for the business card.

regards
Ormund
Updates

Hello Everyone!

Thanks for submitting your designs. 

Yet to find the right design. Probably the below links will give you guys some more idea on what we would like.

Minimalist design with some creativity.

Ormund

http://plaincardgallery.example/inspiration/15-beautifully-minimal-business-cards

http://www.quietlayouthub.example/2011/11/14/30-minimalist-business-card-design/

http://www.firmpixelnotes.example/inspiration/minimal-business-cards/

Target Market(s)

Industrial users

Industry/Entity Type

Industrial

Requirements
Must have
• - Minimalistic design

- Back side of the card should include the manufacturer BRAVOLINE CANADA's decal. The file is upload for the reference

- Further information
Company Name:
KESTRAL SUPPLY COMPANY LLC
Address:
PO Box 9087, Sharjah Industrial Area 5, Qutrani Road
Sharjah, United Arab Emirates
Telephone:
+971-6-5018-392
Fax:
+977-6-5018-393
Email:
mail@ksc-holding.example

- FYI, Kestral Supply Company LLC is the authorised distributor for BRAVOLINE CANADA in the UAE. For further information on bravoline please visit the website www.bravoline.example

```html
<!DOCTYPE html>
<html lang="en">
<head>
<meta charset="utf-8">
<title>Kestral Supply Company LLC – Business Card</title>
<link rel="stylesheet" href="https://fonts.googleapis.com/css2?family=Open+Sans:wght@400;600;700&display=swap">
<style>
  :root {
    --page-bg: #e9e6e2;
    --card-bg: #1f1f1f;
    --card-bg-light: #2a2a2a;
    --text-light: #ffffff;
    --band-grey: #7b7b7b;
    --mark-grey: #8c8c8c;
  }
  * { box-sizing: border-box; margin: 0; padding: 0; }
  html, body {
    width: 1200px;
    height: 960px;
    overflow: hidden;
    background: var(--page-bg);
    font-family: "Open Sans", sans-serif;
  }
  .stage {
    position: relative;
    width: 1200px;
    height: 960px;
  }
  .card {
    position: absolute;
    width: 640px;
    height: 380px;
    background: radial-gradient(ellipse at 40% 30%, var(--card-bg-light), var(--card-bg) 70%);
    color: var(--text-light);
    box-shadow: 0 6px 18px rgba(0, 0, 0, 0.25);
    overflow: hidden;
  }
  .card--front { left: 80px; top: 70px; }
  .card--back { left: 480px; top: 510px; }

  .brand-mark {
    display: flex;
    align-items: center;
    justify-content: center;
    gap: 14px;
  }
  .brand-mark__square {
    background: var(--mark-grey);
    border-radius: 6px;
  }
  .brand-mark__name {
    font-weight: 700;
    color: var(--text-light);
    letter-spacing: 0.04em;
  }

  .card--front .brand-mark { position: absolute; top: 110px; left: 0; right: 0; }
  .card--front .brand-mark__square { width: 56px; height: 56px; }
  .card--front .brand-mark__name { font-size: 30px; }
  .card--front .company-name {
    position: absolute;
    top: 250px;
    left: 0; right: 0;
    text-align: center;
    font-weight: 600;
    font-size: 22px;
  }

  .card--back .brand-mark { position: absolute; top: 36px; left: 0; right: 0; }
  .card--back .brand-mark__square { width: 30px; height: 30px; }
  .card--back .brand-mark__name { font-size: 17px; }
  .card--back .company-name {
    position: absolute;
    top: 92px;
    left: 0; right: 0;
    text-align: center;
    font-weight: 600;
    font-size: 19px;
  }
  .contact {
    position: absolute;
    top: 126px;
    left: 0; right: 0;
    text-align: center;
    font-size: 15px;
    line-height: 25px;
    font-style: normal;
  }
  .band {
    position: absolute;
    left: 0; right: 0;
    background: var(--band-grey);
  }
  .band--thin { top: 252px; height: 30px; }
  .band--thick { top: 320px; height: 30px; }
  .email {
    position: absolute;
    top: 288px;
    left: 0; right: 0;
    text-align: center;
    font-size: 15px;
  }
</style>
</head>
<body>
  <main class="stage">
    <section class="card card--front" aria-label="Card front">
      <div class="brand-mark">
        <span class="brand-mark__square"></span>
        <span class="brand-mark__name">KESTRAL</span>
      </div>
      <h1 class="company-name">KESTRAL SUPPLY COMPANY LLC</h1>
    </section>

    <section class="card card--back" aria-label="Card back">
      <div class="brand-mark">
        <span class="brand-mark__square"></span>
        <span class="brand-mark__name">KESTRAL</span>
      </div>
      <h2 class="company-name">KESTRAL SUPPLY COMPANY LLC</h2>
      <address class="contact">
        Address : PO Box 9087, Sharjah Industrial Area 5,<br>
        Qutrani Road Sharjah, United Arab Emirates<br>
        Telephone : +971-6-5018-392<br>
        Fax : +977-6-5018-393
      </address>
      <div class="band band--thin"></div>
      <p class="email">mail@ksc-holding.example</p>
      <div class="band band--thick"></div>
    </section>
  </main>
</body>
</html>
```